Verra needs a new design we have an updated logo and want a high qualitative high end feel

feel and aesthetic should be high qualitative like the packaging in a zuvi or the qualatative weight/feel of an zuvi design. modern, elegant bold.probably just the verra logo on the backone vesion could be blue background white letter ... open to ideas
Target Market(s)
legal, insurance , medical, finance rho 740
Industry/Entity Type
Information Technology
Font styles to use
Serif

```html
<!DOCTYPE html>
<html lang="en">
<head>
<meta charset="utf-8">
<title>Verra Business Card</title>
<link rel="stylesheet" href="https://fonts.googleapis.com/css2?family=Tinos:wght@400;700&display=swap">
<style>
  :root {
    --navy: #1d2e47;
    --navy-deep: #182740;
    --paper: #f7f7f8;
    --ink: #1d2e47;
    --muted-blue: #4e6f9c;
    --stage: #26272a;
    --white: #ffffff;
  }
  * { margin: 0; padding: 0; box-sizing: border-box; }
  html, body {
    width: 1200px; height: 900px; overflow: hidden;
    background: var(--stage);
    font-family: "Tinos", "Times New Roman", serif;
  }
  .canvas {
    position: relative; width: 1200px; height: 900px;
    display: flex; flex-direction: column; align-items: center; justify-content: center; gap: 60px;
  }
  .card {
    position: relative; width: 560px; height: 320px;
    box-shadow: 0 12px 30px rgba(0,0,0,.45);
  }
  /* Front */
  .card-front {
    background: radial-gradient(ellipse at 40% 40%, #ffffff 0%, var(--paper) 70%, #ececee 100%);
    border-bottom: 10px solid var(--navy);
    display: flex; align-items: center;
  }
  .front-brand {
    width: 300px; padding-left: 50px;
    display: flex; flex-direction: column; align-items: flex-start;
  }
  .wordmark {
    display: flex; align-items: center; gap: 10px;
    font-weight: 700; font-size: 64px; line-height: 1; letter-spacing: 1px;
  }
  .wordmark-dot { width: 14px; height: 14px; border-radius: 50%; }
  .front-brand .wordmark { color: var(--ink); }
  .front-brand .wordmark-dot { background: var(--ink); }
  .brand-descriptor {
    margin: 8px 0 0 150px; font-size: 11px; line-height: 1.15;
    text-transform: uppercase; letter-spacing: 1px; color: var(--ink);
  }
  .divider { width: 1px; height: 140px; background: var(--ink); margin-right: 24px; }
  .contact { color: var(--ink); }
  .contact-name { font-weight: 700; font-size: 19px; }
  .contact-title { font-size: 15px; color: var(--muted-blue); margin-bottom: 8px; }
  .contact-line { display: flex; align-items: center; gap: 8px; font-size: 15px; line-height: 1.4; }
  .contact-line svg { width: 13px; height: 13px; flex: none; fill: var(--ink); }
  /* Back */
  .card-back {
    background: linear-gradient(135deg, var(--navy) 0%, var(--navy-deep) 100%);
    display: flex; flex-direction: column; align-items: center; justify-content: center;
  }
  .card-back .wordmark { color: var(--white); font-size: 76px; }
  .card-back .wordmark-dot { background: var(--white); }
  .card-back .brand-descriptor { color: #cfd6e2; margin-left: 200px; }
  .back-url {
    position: absolute; left: 40px; bottom: 34px;
    color: var(--white); font-size: 15px; letter-spacing: .5px;
  }
</style>
</head>
<body>
<main class="canvas">
  <section class="card card-front">
    <div class="front-brand">
      <div class="wordmark"><span class="wordmark-dot"></span>verra</div>
      <div class="brand-descriptor">Managed<br>Services<br>Group, Inc.</div>
    </div>
    <div class="divider"></div>
    <div class="contact">
      <div class="contact-name">Marcus Ellery</div>
      <div class="contact-title">CEO/Founder</div>
      <div class="contact-line">
        <svg viewBox="0 0 16 16"><path d="M3.6 1.2l2.3 2.6-1.3 1.9c.9 2 2.6 3.8 4.7 4.7l1.9-1.3 2.6 2.3-1.5 2.3C7 13.4 2.6 9 1.3 2.7z"/></svg>
        555-014-2738
      </div>
      <div class="contact-line">
        <svg viewBox="0 0 16 16"><path d="M3.6 1.2l2.3 2.6-1.3 1.9c.9 2 2.6 3.8 4.7 4.7l1.9-1.3 2.6 2.3-1.5 2.3C7 13.4 2.6 9 1.3 2.7z"/></svg>
        555-014-2738
      </div>
      <div class="contact-line">
        <svg viewBox="0 0 16 16"><path d="M1 3h14v10H1z M1.6 3.5L8 9l6.4-5.5" stroke="#fff" stroke-width=".9"/></svg>
        info@verramanagedservices.com
      </div>
      <div class="contact-line">
        <svg viewBox="0 0 16 16"><circle cx="8" cy="8" r="7"/><path d="M1 8h14M8 1c-2.5 3-2.5 11 0 14M8 1c2.5 3 2.5 11 0 14" stroke="#fff" stroke-width=".8" fill="none"/></svg>
        www.verramanagedservices.com
      </div>
    </div>
  </section>

  <section class="card card-back">
    <div class="wordmark"><span class="wordmark-dot"></span>verra</div>
    <div class="brand-descriptor">Managed<br>Services<br>Group, Inc.</div>
    <div class="back-url">www.verramanagedservices.com</div>
  </section>
</main>
</body>
</html>
```